Waste management company seeks a new website design

We need a website design for an environmental services company called 'Vilumetsa Kogumisteenused.' We manage waste collection and recycling for 100K+ households and businesses across Estonia. Please use logos and colors from attached CVI file. The design should be extensively usable for our self-service portal and have a mobile-first approach as it will be turned into an app in the future. The new website should highlight our commitment to sustainability and provide easy access to our services with a clean, modern design. UX inspiration from https://trevix.eu/et-ee/

```html
<!DOCTYPE html>
<html lang="en">
<head>
<meta charset="utf-8">
<title>Vilumetsa Kogumisteenused – Home</title>
<link href="https://fonts.googleapis.com/css2?family=Poppins:wght@400;500;600;700;800&display=swap" rel="stylesheet">
<style>
:root{
  --lime:#d4e000;
  --ink:#1d1d1d;
  --text:#444;
  --muted:#666;
  --brown:#9b8580;
  --cream:#f8fae6;
  --forest:#063a1d;
  --forest-deep:#042a14;
  --sky:#bde8ec;
  --white:#fff;
}
*{margin:0;padding:0;box-sizing:border-box}
html,body{width:1200px;height:1200px;overflow:hidden;background:var(--white);font-family:'Poppins',sans-serif;color:var(--ink)}
.stage{position:absolute;left:0;top:0;width:1932px;height:1932px;transform:scale(.621118);transform-origin:0 0}
.page{position:absolute;left:605px;top:0;width:721px;height:1932px;background:var(--white);overflow:hidden}
.abs{position:absolute}

/* top bar */
.topbar{left:0;top:0;width:721px;height:21px;background:var(--lime);font-size:6.5px;color:var(--ink)}
.topbar .contact{position:absolute;top:6px;display:flex;align-items:center;gap:3px}
.social-dot{position:absolute;top:5px;width:11px;height:11px;border-radius:50%;background:var(--white)}

/* header */
.header{left:0;top:21px;width:721px;height:46px}
.brand{position:absolute;display:flex;align-items:center;gap:5px;font-weight:500}
.brand .mark{width:22px;height:22px;border-radius:50%;background:var(--lime);flex:none}
.brand .name{line-height:1.05}
.header .brand{left:119px;top:12px;font-size:8.5px;color:var(--brown)}
.nav a{position:absolute;top:20px;font-size:6.3px;font-weight:600;color:var(--ink);text-decoration:none}
.nav a.active{color:var(--brown);font-weight:500}
.nav .underline{position:absolute;left:303px;top:44px;width:17px;height:2px;background:var(--lime)}
.btn{position:absolute;display:flex;align-items:center;justify-content:center;border-radius:12px;font-weight:600;text-decoration:none}
.btn-brown{background:var(--brown);color:var(--white);font-size:6.3px;letter-spacing:.1px}
.btn-lime{background:var(--lime);color:var(--ink);font-size:6.3px}
.btn-dark{background:#222;color:var(--white);font-size:6.3px}

/* hero */
.hero{left:0;top:67px;width:721px;height:405px;background:linear-gradient(180deg,#3f4a25 0%,#6b6a34 30%,#5b4a2a 60%,#2f2a1c 100%)}
.hero h1{position:absolute;left:119px;top:107px;font-size:32px;font-weight:800;line-height:1.1;color:var(--white);letter-spacing:-.3px}
.hero h1 span{color:var(--lime)}

/* welcome */
.welcome{left:0;top:470px;width:721px;height:270px;background:linear-gradient(180deg,var(--white) 0%,var(--cream) 100%)}
.photo{background:linear-gradient(160deg,#a88a5a,#6d8f3d 45%,#2f7a52 70%,#8a5a3a)}
.frame{position:absolute;left:114px;top:-4px;width:172px;height:216px;background:var(--lime);transform:rotate(-2deg);border-radius:3px}
.section-icon{width:11px;height:11px;border-radius:50%;background:var(--lime);position:absolute}
.eyebrow{position:absolute;font-size:6.5px;font-weight:600;letter-spacing:2.2px;color:var(--lime)}
.h2{position:absolute;font-weight:700;color:var(--ink);line-height:1.1}
.lead{position:absolute;font-size:6.6px;line-height:11.2px;color:var(--text)}

/* services */
.svc-title{position:absolute;font-size:11.5px;font-weight:600;text-align:center;line-height:1.1;color:var(--ink)}
.svc-box{position:absolute;width:115px;height:60px;background:var(--lime)}

/* banner */
.banner{left:0;top:1053px;width:721px;height:181px;background:var(--sky);overflow:hidden}
.banner h3{position:absolute;left:0;width:721px;top:34px;text-align:center;font-size:23px;font-weight:800;line-height:32px;color:#111}

/* news */
.news-img{position:absolute;width:154px;height:132px;border-radius:6px 6px 0 0}
.date{position:absolute;width:32px;height:28px;background:var(--lime);border-radius:0 0 14px 14px;text-align:center;font-weight:700;font-size:11px;line-height:11px;padding-top:3px}
.date small{display:block;font-size:5px;font-weight:600;line-height:7px}
.news-card{position:absolute;width:131px;height:92px;background:var(--white);border:1px solid #e6e6e6;border-radius:4px}
.news-card h4{position:absolute;left:11px;top:9px;font-size:7.6px;font-weight:600;line-height:11px;color:var(--ink)}
.news-card p{position:absolute;left:11px;top:36px;width:110px;font-size:5.8px;line-height:10px;color:var(--muted)}
.dot{position:absolute;top:1625px;width:5px;height:5px;border-radius:50%;border:1px solid #999}

/* footer */
.footer{left:0;top:1640px;width:721px;height:292px;background:var(--forest)}
.footer .brand{left:119px;top:124px;font-size:8.5px;color:var(--white)}
.f-text{position:absolute;font-size:6.2px;line-height:10.5px;color:#e8efe9}
.f-head{position:absolute;font-size:7.8px;font-weight:600;color:var(--lime)}
.f-list{position:absolute;list-style:none;font-size:6.2px;color:#e8efe9}
.f-list li{height:17px}
.f-social{position:absolute;top:207px;width:15px;height:15px;border-radius:50%;background:var(--white)}
.f-contact{position:absolute;display:flex;gap:5px;font-size:6.2px;line-height:9.3px;color:#e8efe9}
.bottom{position:absolute;left:0;top:257px;width:721px;height:35px;background:var(--forest-deep);font-size:6px;color:#dfe7e1}
</style>
</head>
<body>
<div class="stage">
<div class="page">

  <!-- top bar -->
  <div class="abs topbar">
    <div class="contact" style="left:119px">
      <svg width="8" height="6" viewBox="0 0 8 6"><rect x=".5" y=".5" width="7" height="5" fill="none" stroke="#1d1d1d" stroke-width=".7"/><path d="M.5 .5 4 3.3 7.5 .5" fill="none" stroke="#1d1d1d" stroke-width=".7"/></svg>
      info@vilumetsa.ee
    </div>
    <div class="contact" style="left:234px">
      <svg width="8" height="8" viewBox="0 0 8 8"><path d="M1.5 .8 3 .8 3.6 2.5 2.7 3.2Q3.4 4.7 4.8 5.4L5.5 4.5 7.2 5.1 7.2 6.6Q7 7.4 6 7.3 .8 6.5.7 1.8.7 .9 1.5.8Z" fill="none" stroke="#1d1d1d" stroke-width=".7"/></svg>
      (+372) 655 12 34
    </div>
    <span class="social-dot" style="left:561px"></span>
    <span class="social-dot" style="left:576px"></span>
    <span class="social-dot" style="left:591px"></span>
  </div>

  <!-- header -->
  <header class="abs header">
    <div class="brand"><span class="mark"></span><span class="name">Vilumetsa<br>Kogumisteenused</span></div>
    <nav class="nav">
      <a class="active" href="#" style="left:303px">HOME</a>
      <a href="#" style="left:339px">ABOUT</a>
      <a href="#" style="left:378px">OUR SERVICES ⌄</a>
      <a href="#" style="left:439px">INDUSTRIES</a>
      <a href="#" style="left:492px">NEWS</a>
      <span class="underline"></span>
    </nav>
    <a class="btn btn-brown" href="#" style="left:523px;top:12px;width:80px;height:22px">QUICK CONTACT</a>
  </header>

  <!-- hero -->
  <section class="abs hero" role="img" aria-label="Photo of a row of colourful waste bins along a park path at sunset">
    <h1><span>Green Solutions</span><br>for Clean Communities</h1>
    <a class="btn btn-lime" href="#" style="left:122px;top:208px;width:80px;height:22px">QUICK CONTACT</a>
    <svg class="abs" style="left:0;top:0" width="721" height="405" viewBox="0 0 721 405">
      <path d="M0 393 Q120 322 250 324 Q430 328 570 385 Q650 408 721 400 L721 405 L0 405 Z" fill="#fff"/>
      <path d="M0 368 Q80 330 185 327 Q90 338 0 393 Z" fill="#d4e000"/>
    </svg>
  </section>

  <!-- welcome -->
  <section class="abs welcome">
    <div class="frame"></div>
    <div class="abs photo" role="img" aria-label="Photo of a green recycling bag filled with bottles and vegetables on the ground" style="left:119px;top:0;width:169px;height:209px;border-radius:4px"></div>
    <span class="section-icon" style="left:320px;top:5px"></span>
    <div class="eyebrow" style="left:320px;top:22px">WELCOME TO</div>
    <h2 class="h2" style="left:320px;top:33px;font-size:25px;line-height:28px">Eco-Friendly<br>Waste Management</h2>
    <p class="lead" style="left:320px;top:106px;width:285px">We are dedicated to providing reliable and efficient waste collection services that help keep our communities clean and sustainable. With a commitment to environmental responsibility and customer satisfaction, we offer comprehensive waste management solutions tailored to meet the needs of both residential and commercial clients.</p>
    <a class="btn btn-lime" href="#" style="left:320px;top:182px;width:66px;height:22px">LEARN MORE</a>
  </section>

  <!-- services -->
  <span class="section-icon" style="left:354px;top:783px"></span>
  <div class="eyebrow" style="left:0;width:721px;text-align:center;top:800px">WASTE MANAGEMENT MADE EASY</div>
  <h2 class="h2" style="left:0;width:721px;text-align:center;top:810px;font-size:25px">Our Services</h2>

  <div class="abs photo" role="img" aria-label="Photo of a garbage truck collecting residential bins" style="left:119px;top:869px;width:143px;height:92px;background:linear-gradient(160deg,#8aa07a,#6c7468 50%,#4d5a44)"></div>
  <div class="svc-box" style="left:133px;top:931px"></div>
  <div class="svc-title" style="left:133px;width:115px;top:949px">Residential<br>Waste Collection</div>
  <a class="btn btn-dark" href="#" style="left:160px;top:982px;width:61px;height:17px">Get Started</a>

  <div class="abs photo" role="img" aria-label="Photo of hands in orange gloves tying a black rubbish bag" style="left:289px;top:869px;width:144px;height:92px;background:linear-gradient(160deg,#cfc6c0,#e06a2a 40%,#2a2a2a 60%,#b8322f)"></div>
  <div class="svc-box" style="left:303px;top:931px"></div>
  <div class="svc-title" style="left:303px;width:115px;top:949px">Bulk<br>Waste Removal</div>
  <a class="btn btn-dark" href="#" style="left:330px;top:982px;width:61px;height:17px">Get Started</a>

  <div class="abs photo" role="img" aria-label="Photo of volunteers in green shirts collecting litter in a park" style="left:460px;top:869px;width:143px;height:92px;background:linear-gradient(160deg,#b9b2a0,#6f8f4e 45%,#3fae4a 70%,#4e6a3a)"></div>
  <div class="svc-box" style="left:474px;top:931px"></div>
  <div class="svc-title" style="left:474px;width:115px;top:949px">Green<br>Waste Collection</div>
  <a class="btn btn-dark" href="#" style="left:501px;top:982px;width:61px;height:17px">Get Started</a>

  <!-- banner -->
  <section class="abs banner">
    <div class="abs" role="img" aria-label="Illustration of green rolling hills with a worker holding a recycling bag beside a green bin" style="left:0;top:0;width:721px;height:181px;background:linear-gradient(180deg,rgba(0,0,0,0) 40%,#5fbf2a 62%,#3f9a1e 100%)"></div>
    <h3>We Take Care of Your<br>Waste Responsibly</h3>
    <a class="btn btn-lime" href="#" style="left:309px;top:113px;width:104px;height:28px;border-radius:14px;font-size:7.5px">Request Pickup</a>
  </section>

  <!-- news -->
  <span class="section-icon" style="left:354px;top:1289px"></span>
  <div class="eyebrow" style="left:0;width:721px;text-align:center;top:1305px">OUR NEWS FROM BLOG</div>
  <h2 class="h2" style="left:0;width:721px;text-align:center;top:1316px;font-size:25px">Latest News</h2>

  <div class="news-img photo" role="img" aria-label="Photo of a person dropping waste into grey sorting bins" style="left:119px;top:1381px;background:linear-gradient(160deg,#7fa05a,#8a8f8c 50%,#505654)"></div>
  <div class="date" style="left:130px;top:1381px">10<small>JLY</small></div>
  <div class="news-card" style="left:130px;top:1493px">
    <h4>Our commitment to<br>Sustainability</h4>
    <p>Our mission is to make waste col-lection simple, efficient, and eco-friendly.</p>
  </div>
  <a class="btn btn-lime" href="#" style="left:142px;top:1574px;width:60px;height:22px;border-radius:11px">Read More ➔</a>

  <div class="news-img photo" role="img" aria-label="Photo of plastic bottles piled in a recycling container" style="left:284px;top:1381px;background:linear-gradient(160deg,#e9e4dc,#6fb7e0 40%,#7fd0b8 70%,#2f8f5a)"></div>
  <div class="date" style="left:296px;top:1381px">05<small>JUN</small></div>
  <div class="news-card" style="left:296px;top:1493px">
    <h4>Prioritize customer<br>satisfaction</h4>
    <p>Our mission is to make waste col-lection simple, efficient, and eco-friendly.</p>
  </div>
  <a class="btn btn-lime" href="#" style="left:308px;top:1574px;width:60px;height:22px;border-radius:11px">Read More ➔</a>

  <div class="news-img photo" role="img" aria-label="Photo of a worker in a hi-vis vest picking litter into a white bag on grass" style="left:450px;top:1381px;background:linear-gradient(160deg,#6f8a3c,#d9d37a 45%,#5f7f2f 75%,#48602a)"></div>
  <div class="date" style="left:461px;top:1381px">15<small>MAY</small></div>
  <div class="news-card" style="left:461px;top:1493px">
    <h4>Reliable and timely<br>collection</h4>
    <p>Our mission is to make waste col-lection simple, efficient, and eco-friendly.</p>
  </div>
  <a class="btn btn-lime" href="#" style="left:473px;top:1574px;width:60px;height:22px;border-radius:11px">Read More ➔</a>

  <span class="dot" style="left:345px;background:var(--lime);border-color:var(--lime)"></span>
  <span class="dot" style="left:354px"></span>
  <span class="dot" style="left:363px"></span>
  <span class="dot" style="left:371px"></span>

  <!-- footer -->
  <footer class="abs footer">
    <svg class="abs" style="left:0;top:0" width="721" height="100" viewBox="0 0 721 100">
      <path d="M0 0 L721 0 L721 48 Q640 88 545 88 Q330 82 140 14 Q70 -2 0 12 Z" fill="#fff"/>
      <path d="M721 14 Q660 70 545 86 Q650 82 721 48 Z" fill="#d4e000"/>
    </svg>
    <div class="brand"><span class="mark"></span><span class="name">Vilumetsa<br>Kogumisteenused</span></div>
    <p class="f-text" style="left:119px;top:162px;width:128px">Lorem Ipsum is simply dummy text of the printing and typesetting industry. Lorem Ipsum has been the industry.</p>
    <span class="f-social" style="left:119px"></span>
    <span class="f-social" style="left:142px"></span>
    <span class="f-social" style="left:165px"></span>

    <div class="f-head" style="left:293px;top:116px">Quick Links</div>
    <ul class="f-list" style="left:293px;top:137px">
      <li>Home</li><li>About</li><li>Our Services</li><li>Industries</li><li>News</li><li>Contact</li>
    </ul>
    <div class="f-head" style="left:375px;top:116px">Services</div>
    <ul class="f-list" style="left:375px;top:137px">
      <li>Residential Waste Collection</li><li>Commercial Waste Collection</li><li>Bulk Waste Removal</li><li>Green Waste Collection</li><li>Hazardous Waste Disposal</li>
    </ul>
    <div class="f-head" style="left:505px;top:116px">Contact Us</div>
    <div class="f-contact" style="left:505px;top:137px">
      <svg width="8" height="9" viewBox="0 0 8 9"><path d="M4 8.5Q1 5.3 1 3.4A3 3 0 0 1 7 3.4Q7 5.3 4 8.5Z" fill="none" stroke="#e8efe9" stroke-width=".7"/><circle cx="4" cy="3.4" r="1" fill="none" stroke="#e8efe9" stroke-width=".7"/></svg>
      <span>AS Vilumetsa Kogumisteenused<br>Kivimurru 8, Tallinn 10411<br>Registrikood: 10554321</span>
    </div>
    <div class="f-contact" style="left:505px;top:174px">
      <svg width="8" height="8" viewBox="0 0 8 8"><path d="M1.5 .8 3 .8 3.6 2.5 2.7 3.2Q3.4 4.7 4.8 5.4L5.5 4.5 7.2 5.1 7.2 6.6Q7 7.4 6 7.3 .8 6.5.7 1.8.7 .9 1.5.8Z" fill="none" stroke="#e8efe9" stroke-width=".7"/></svg>
      <span>(+372) 655 12 34</span>
    </div>
    <div class="f-contact" style="left:505px;top:191px">
      <svg width="8" height="6" viewBox="0 0 8 6"><rect x=".5" y=".5" width="7" height="5" fill="none" stroke="#e8efe9" stroke-width=".7"/><path d="M.5 .5 4 3.3 7.5 .5" fill="none" stroke="#e8efe9" stroke-width=".7"/></svg>
      <span>info@vilumetsa.ee</span>
    </div>

    <div class="bottom">
      <span class="abs" style="left:119px;top:13px">© Vilumetsa Kogumisteenused 2024 | All Rights Reserved.</span>
      <span class="abs" style="right:118px;top:13px">Conditions &nbsp;|&nbsp; Privacy</span>
    </div>
  </footer>

</div>
</div>
</body>
</html>
```